Newly opened kids play space needs brochure to show what our space has to offer

Tri-fold color brochure with same aethetic as website (www.fernhollowplayhouse.com) that provides a comprehensive and visual overview of what our play space is comprised of. Features of the brochure should include our logo, "A Steiner and Reggio-inspired Play Space in the Poconos", photos of: Dedicated Infant Play Area; Cafe and Free WiFi; Weekly Themed Activities; Unique Classes; Parties and Events. Photos also of our open play area with children playing within it. Info within the brochure should include our location, hours. Please take some copy from : https://www.facebook.com/fernhollowkinderplayhouse/?ref=bookmarks
and from the Plan Your Visit part of the website. I have a lot of photos to use; is there a way to put in generic photo placeholders and I can pick which photos of mine to go into the various areas of the brochure, or if you need the photos ahead of time, please let me know the best way to proceed. I am attaching the logo files for now.

Font styles to use
Sans Serif

Colors
85cae6
cee9f5
86cfc6
cfeae6
fdf9cf
fff3d1
eaf2ce
cadf82

Requirements
Must have
• Eye catching placement of photos; color scheme similar to website and logo colors
Should not have
• Brochure should be simple, not too colorful - no primary colors, not too crowded.

```html
<!DOCTYPE html>
<html lang="en">
<head>
<meta charset="utf-8">
<title>Fern Hollow – Plan Your Visit</title>
<link rel="stylesheet" href="https://fonts.googleapis.com/css2?family=Oswald:wght@500;600&family=Roboto+Condensed:wght@400;700&display=swap">
<style>
:root{
  --brown:#6a3a1e;
  --ink:#2e2a26;
  --sky:#85cae6;
  --sky-pale:#cee9f5;
  --mint:#86cfc6;
  --mint-pale:#cfeae6;
  --cream:#fdf9cf;
  --butter:#fff3d1;
  --sage-pale:#eaf2ce;
  --sage:#cadf82;
  --logo-teal:#2f9bb5;
}
*{margin:0;padding:0;box-sizing:border-box}
html,body{width:1200px;height:1000px;overflow:hidden}
body{font-family:"Roboto Condensed",sans-serif;color:var(--ink)}
.canvas{
  position:relative;width:1200px;height:1000px;overflow:hidden;
  background:
    radial-gradient(ellipse 420px 320px at 150px 420px,rgba(202,223,130,.55),transparent 70%),
    radial-gradient(ellipse 380px 260px at 620px 60px,rgba(202,223,130,.45),transparent 70%),
    radial-gradient(ellipse 300px 220px at 1120px 140px,rgba(234,242,206,.9),transparent 70%),
    radial-gradient(ellipse 360px 260px at 300px 760px,rgba(253,249,207,.9),transparent 70%),
    linear-gradient(160deg,var(--sage-pale) 0%,#f6f9e8 45%,#f4f8e2 100%);
}
.bottom-band{position:absolute;left:0;top:808px;width:1200px;height:192px;background:linear-gradient(180deg,#fbf8d6,var(--cream))}
.photo{position:absolute}
.photo--framed{border:6px solid #fff;box-shadow:0 1px 3px rgba(0,0,0,.12)}
.ph-ship{left:8px;top:8px;width:174px;height:160px;background:linear-gradient(160deg,#c9a9a0,#3f9bb3 80%)}
.ph-crafts{left:185px;top:82px;width:200px;height:238px;background:linear-gradient(160deg,#c7c3bd,#8b5e4a)}
.ph-facepaint{left:38px;top:298px;width:206px;height:196px;background:linear-gradient(160deg,#9cc96f,#a48a77)}
.ph-flowers{left:170px;top:478px;width:216px;height:240px;background:linear-gradient(160deg,#b3b9c0,#d8b78a)}

.heading{position:absolute;right:17px;top:56px;font-family:Oswald,sans-serif;font-weight:600;font-size:42px;letter-spacing:.5px;color:var(--brown);text-shadow:2px 2px 0 rgba(106,58,30,.25);line-height:1;padding-bottom:4px;border-bottom:3px solid var(--brown)}
.intro{position:absolute;right:17px;top:141px;width:720px;text-align:right;font-size:21px;line-height:33px}
.divider{position:absolute;left:403px;top:211px;width:780px;height:4px;background:var(--brown)}

.feature-photo{position:absolute;width:188px;height:230px}
.ph-themed{left:403px;top:267px;background:linear-gradient(160deg,#e2ddd5,#6e5a4c)}
.ph-infant{left:800px;top:267px;width:183px;background:linear-gradient(160deg,#ddd8d0,#3b3a3e)}
.ph-classes{left:403px;top:533px;height:228px;background:linear-gradient(160deg,#3d86b2,#d28a4f)}
.ph-cafe{left:800px;top:532px;width:183px;background:linear-gradient(160deg,#8aa0a8,#b9805a)}

.feature{position:absolute;width:190px}
.feature h2{font-family:Oswald,sans-serif;font-weight:600;font-size:25px;line-height:35px;color:var(--brown);text-align:center;margin-bottom:8px}
.feature p{font-size:15.5px;line-height:20px;text-align:justify}
.f-themed{left:599px;top:283px}
.f-infant{left:988px;top:283px;width:196px}
.f-classes{left:599px;top:573px}
.f-cafe{left:988px;top:573px;width:196px}
.f-classes h2,.f-cafe h2{text-align:left;margin-bottom:10px}

.brand{position:absolute;left:52px;top:830px;width:270px;text-align:center}
.brand-name{display:flex;align-items:center;justify-content:center;gap:10px;font-family:"Roboto Condensed",sans-serif;font-weight:700;font-size:58px;line-height:1;color:var(--logo-teal)}
.brand-dot{width:22px;height:22px;border-radius:50%;background:var(--mint)}
.brand-tag{margin-top:10px;font-size:20px;font-weight:700;color:var(--logo-teal)}

.ph-easel{left:578px;top:790px;width:108px;height:152px;background:linear-gradient(160deg,#e3c79a,#9aa56a)}
.slogan{position:absolute;left:410px;top:936px;font-family:"Roboto Condensed",sans-serif;font-weight:700;font-size:33px;color:#fbf1ea;text-shadow:1px 2px 3px rgba(90,60,40,.55)}
.ph-openplay{left:722px;top:808px;width:466px;height:162px;background:linear-gradient(160deg,#d9c9b3,#a06f4d 70%,#2c3a6a);box-shadow:0 3px 8px rgba(0,0,0,.35)}
</style>
</head>
<body>
<main class="canvas">
  <div class="bottom-band"></div>

  <div class="photo photo--framed ph-ship" role="img" aria-label="Photo: wooden pirate ship play structure on a blue rug"></div>
  <div class="photo photo--framed ph-crafts" role="img" aria-label="Photo: children making crafts around a wooden table"></div>
  <div class="photo photo--framed ph-facepaint" role="img" aria-label="Photo: child getting face paint at a party"></div>
  <div class="photo photo--framed ph-flowers" role="img" aria-label="Photo: children with flower crowns doing a nature craft"></div>

  <h1 class="heading">PLAN YOUR VISIT!</h1>
  <p class="intro">Fern Hollow offers open-ended, natural toys and activities that nurture the child's sense of wonder and invites them to explore in our serene and spacious environment.</p>
  <div class="divider"></div>

  <div class="photo feature-photo ph-themed" role="img" aria-label="Photo: children planting flowers in pots"></div>
  <section class="feature f-themed">
    <h2>THEMED<br>ACTIVITIES</h2>
    <p>Stories, crafts, and activities change weekly to celebrate the seasons and the world around us.</p>
  </section>

  <div class="photo feature-photo ph-infant" role="img" aria-label="Photo: parent with baby in the infant area"></div>
  <section class="feature f-infant">
    <h2>DEDICATED<br>INFANT AREA</h2>
    <p>Bond safely with your baby while being within eyeshot of the main play area.</p>
  </section>

  <div class="photo feature-photo ph-classes" role="img" aria-label="Photo: children sitting in a circle on a colourful rug"></div>
  <section class="feature f-classes">
    <h2>UNIQUE CLASSES</h2>
    <p>Our multi-age, multi-sensory approach to traditional classes nurtures the whole child in a creative and fun way.</p>
  </section>

  <div class="photo feature-photo ph-cafe" role="img" aria-label="Photo: parent enjoying coffee at the cafe"></div>
  <section class="feature f-cafe">
    <h2>CAFE AND WIFI</h2>
    <p>Take a break or catch up on work while enjoying Brewhaven coffee, beverages, and healthy snacks.</p>
  </section>

  <div class="brand">
    <div class="brand-name"><span class="brand-dot"></span>fern hollow</div>
    <div class="brand-tag">A Kinderhaus Play Space</div>
  </div>

  <div class="photo ph-easel" role="img" aria-label="Illustration: small wooden easel with painted tree"></div>
  <p class="slogan">Play. Learn. Grow.</p>
  <div class="photo ph-openplay" role="img" aria-label="Photo: children playing in the open play area"></div>
</main>
</body>
</html>
```